Letterhead and Envelope Design for Investment Company

We need a letterhead and envelope design.
We are a family owned investment company doing direct investments into other family owned businesses.
I have attached all our current marketing material including our logo for reference.

Our under construction website can be found here:
https://rob-darke-qv7m.pagevorlo.com/
password: Copperfen

Target Market(s)

Bankers, business owners, financial partners

Industry/Entity Type

Investment

Colors

Designer to choose colors to be used in the design.

Requirements
Must have
• Logo, and company information

```html
<!DOCTYPE html>
<html lang="en">
<head>
<meta charset="utf-8">
<title>Copperfen Holdings – Letterhead and Envelope</title>
<link href="https://fonts.googleapis.com/css2?family=Source+Sans+3:wght@400&display=swap" rel="stylesheet">
<style>
  :root {
    --gold: #BA8A2E;
    --paper: #FFFFFF;
    --ink: #231F20;
    --bg-start: #A1005E;
    --bg-mid: #4A0038;
    --bg-end: #0E0024;
  }
  * { box-sizing: border-box; margin: 0; padding: 0; }
  html, body { width: 1200px; height: 900px; overflow: hidden; }
  body {
    position: relative;
    font-family: "Source Sans 3", sans-serif;
    font-weight: 400;
    background: linear-gradient(135deg, var(--bg-start) 0%, var(--bg-mid) 40%, var(--bg-end) 75%);
  }
  .sheet {
    position: absolute;
    background: var(--paper);
    overflow: hidden;
  }
  .letterhead { left: 78px; top: 133px; width: 490px; height: 634px; }
  .envelope-front { left: 589px; top: 210px; width: 548px; height: 230px; }
  .envelope-back { left: 589px; top: 490px; width: 548px; height: 230px; }

  .band { position: absolute; left: 0; top: 0; }

  .wordmark {
    position: absolute;
    color: var(--paper);
    text-transform: uppercase;
    letter-spacing: 0.06em;
    white-space: nowrap;
    line-height: 1;
    text-align: center;
  }
  .letterhead .wordmark { left: 25px; top: 37px; width: 110px; font-size: 10px; }
  .envelope-front .wordmark { left: 25px; top: 41px; width: 120px; font-size: 11px; }
  .envelope-back .wordmark { left: 224px; top: 13px; width: 100px; font-size: 7.5px; }

  .contact {
    position: absolute;
    color: var(--ink);
    font-size: 6.6px;
    line-height: 9.2px;
    list-style: none;
  }
  .contact li { position: relative; padding-left: 10px; white-space: nowrap; }
  .contact .icon {
    position: absolute; left: 0; top: 1px;
    width: 7px; height: 7px;
  }
  .letterhead .contact-address { left: 274px; top: 21px; }
  .letterhead .contact-lines { left: 370px; top: 21px; }
  .envelope-front .contact { left: 25px; top: 150px; font-size: 6.8px; line-height: 9.8px; }
  .envelope-front .contact .gap { margin-top: 1px; }
</style>
</head>
<body>

<svg width="0" height="0" style="position:absolute" aria-hidden="true">
  <defs>
    <symbol id="icon-home" viewBox="0 0 10 10">
      <path d="M5 1 L9.5 5 H8 V9 H6 V6.5 H4 V9 H2 V5 H0.5 Z" fill="#BA8A2E"/>
    </symbol>
    <symbol id="icon-phone" viewBox="0 0 10 10">
      <rect x="0.5" y="0.5" width="9" height="9" rx="2" fill="#BA8A2E"/>
      <path d="M3 2.5 C2.5 5 5 7.5 7.5 7 L7.5 6 L6.3 5.5 L5.7 6.1 C4.8 5.6 4.4 5.2 3.9 4.3 L4.5 3.7 L4 2.5 Z" fill="#FFFFFF"/>
    </symbol>
    <symbol id="icon-mail" viewBox="0 0 10 10">
      <rect x="0.5" y="2" width="9" height="6" fill="#BA8A2E"/>
      <path d="M0.8 2.3 L5 5.5 L9.2 2.3" fill="none" stroke="#FFFFFF" stroke-width="0.8"/>
    </symbol>
    <symbol id="icon-web" viewBox="0 0 10 10">
      <circle cx="5" cy="5" r="4.5" fill="#BA8A2E"/>
      <path d="M0.8 5 H9.2 M5 0.6 C2.8 3 2.8 7 5 9.4 M5 0.6 C7.2 3 7.2 7 5 9.4" fill="none" stroke="#FFFFFF" stroke-width="0.6"/>
    </symbol>
  </defs>
</svg>

<section class="sheet letterhead" aria-label="Letterhead">
  <svg class="band" width="490" height="58" viewBox="0 0 490 58" aria-hidden="true">
    <path d="M0 0 H490 V15 H180 C172 15 170 18 166 24 L152 50 C149 56 146 58 138 58 H0 Z" fill="var(--gold)"/>
  </svg>
  <div class="wordmark">Copperfen Holdings</div>
  <ul class="contact contact-address">
    <li><svg class="icon"><use href="#icon-home"/></svg>Copperfen Holdings, Inc.</li>
    <li>415 Linden Ave; Suite 300</li>
    <li>Marlow Falls, IA 52099</li>
  </ul>
  <ul class="contact contact-lines">
    <li><svg class="icon"><use href="#icon-phone"/></svg>555-014-2263</li>
    <li><svg class="icon"><use href="#icon-mail"/></svg>inquiries@copperfenholdings.com</li>
    <li><svg class="icon"><use href="#icon-web"/></svg>copperfenholdings.com</li>
  </ul>
</section>

<section class="sheet envelope-front" aria-label="Envelope front">
  <svg class="band" width="548" height="64" viewBox="0 0 548 64" aria-hidden="true">
    <path d="M0 0 H548 V16 H200 C192 16 190 19 186 26 L170 56 C167 62 163 64 155 64 H0 Z" fill="var(--gold)"/>
  </svg>
  <div class="wordmark">Copperfen Holdings</div>
  <ul class="contact">
    <li><svg class="icon"><use href="#icon-home"/></svg>Copperfen Holdings, Inc.</li>
    <li>415 Linden Ave; Suite 300</li>
    <li>Marlow Falls, IA 52099</li>
    <li class="gap"><svg class="icon"><use href="#icon-phone"/></svg>555-014-2263</li>
    <li><svg class="icon"><use href="#icon-mail"/></svg>inquiries@copperfenholdings.com</li>
    <li><svg class="icon"><use href="#icon-web"/></svg>copperfenholdings.com</li>
  </ul>
</section>

<section class="sheet envelope-back" aria-label="Envelope back">
  <svg class="band" width="548" height="35" viewBox="0 0 548 35" aria-hidden="true">
    <path d="M0 0 H548 L523 35 H26 Z" fill="var(--gold)"/>
  </svg>
  <div class="wordmark">Copperfen Holdings</div>
</section>

</body>
</html>
```